Flyer-Design für Beratung, Coaching
Zielgruppe
Beratung, Coaching, Mediation. Meine Zielgruppe sind insbesondere hochgestellte Führungskräfte /Bereichsleiter, Vorstände, Geschäftsführer und Projektleiter.
Aufgabenstellung
Ich habe das neue Logo (quervoran.kollegen), den ersten Flyer, ein neues Bild und den aktuellen Text des Flyers beigefügt. beigefügt. Ich müsste im fertigen Flyer aber den Text editieren können, da ich gelegentlich neue Passagen einfügen möchte. Der Flyer sollte DIN A4 quer im Format sein, damit ich ihn falten kann. Sofern aber jemand eine andere Idee hat, nur zu. Farblich sollte natürlich das neue Logo die Gestaltung des Flyers beeinflussen. Der Flyer soll als eher exklusives Giving verwendet werden; nicht als 'Massenware'. Ich möchte den Flyer als persönliches Profildokument an ausgewählte Personen weitergeben, die mich bereits aus der Mund-zu-Mund Propaganda kennen.

```html
<!DOCTYPE html>
<html lang="de">
<head>
<meta charset="utf-8">
<title>quervoran.kollegen – Profilflyer</title>
<link rel="stylesheet" href="https://fonts.googleapis.com/css2?family=Open+Sans:wght@300;400;600;700;800&display=swap">
<style>
  :root {
    --canvas: #7b8087;
    --teal: #6a9a9b;
    --teal-dark: #236a70;
    --gold: #b89a55;
    --gold-text: #a9862f;
    --accent-orange: #d9a24d;
    --sand: #c9b47f;
    --sand-light: #e2d6b6;
    --badge-blue: #1f4f9c;
    --badge-sky: #2a8fd0;
    --badge-grey: #c9c9c9;
    --ink: #151515;
    --white: #ffffff;
  }
  * { box-sizing: border-box; margin: 0; padding: 0; }
  html, body { width: 1200px; height: 900px; overflow: hidden; }
  body {
    background: var(--canvas);
    font-family: "Open Sans", Arial, sans-serif;
    color: var(--ink);
    position: relative;
  }
  .page {
    position: absolute;
    left: 260px;
    width: 680px;
    height: 440px;
    background: var(--white);
    overflow: hidden;
  }
  .page--outside { top: 6px; }
  .page--inside { top: 454px; }

  /* ---------- Outside ---------- */
  .qual-panel {
    position: absolute; left: 0; top: 0; width: 363px; height: 440px;
    background: var(--teal);
  }
  .qual-title {
    position: absolute; top: 20px; left: 0; width: 363px;
    display: flex; justify-content: center; align-items: center; gap: 7px;
    font-size: 31px; font-weight: 700; letter-spacing: 0.5px;
  }
  .qual-title .dot { width: 20px; height: 20px; border-radius: 50%; background: var(--gold); }
  .qual-list {
    position: absolute; top: 63px; left: 0; width: 363px;
    text-align: center; font-size: 8.6px; font-weight: 600; line-height: 11.5px;
    word-spacing: 1px;
  }
  .qual-list .entry { margin-bottom: 10px; }
  .qual-list .entry-title { color: var(--white); }
  .qual-list .entry-title.accent { color: var(--accent-orange); }
  .qual-list .entry-place { color: var(--ink); }

  .contact-title {
    position: absolute; top: 224px; left: 0; width: 370px; text-align: center;
    font-size: 18px; font-weight: 600; color: var(--white);
  }
  .contact-frame {
    position: absolute; left: 48px; top: 265px; width: 263px; height: 81px;
    border: 3px solid var(--white); border-top: none; border-right: none;
  }
  .contact-card {
    position: absolute; left: 52px; top: 259px; width: 264px; height: 83px;
    background: var(--gold);
    display: flex; flex-direction: column; justify-content: center; align-items: center;
    font-size: 15.5px; line-height: 21px; color: var(--ink);
    font-weight: 300; font-style: normal;
  }
  .footer-bands { position: absolute; left: 0; top: 361px; width: 380px; height: 60px; }
  .footer-info {
    position: absolute; left: 0; top: 382px; width: 363px; text-align: center;
    font-size: 10.5px; font-weight: 600; line-height: 12.5px; color: var(--ink);
  }

  .brand {
    position: absolute; left: 363px; top: 94px; width: 317px;
    display: flex; justify-content: center; align-items: center; gap: 7px;
    font-size: 19px; font-weight: 600; color: var(--gold-text);
  }
  .brand .mark { width: 10px; height: 10px; border-radius: 50%; background: var(--gold-text); }
  .tagline {
    position: absolute; left: 363px; top: 120px; width: 317px; text-align: center;
    font-size: 5.5px; font-weight: 600; letter-spacing: 2.2px; color: var(--gold-text);
  }
  .portrait {
    position: absolute; left: 441px; top: 128px; width: 194px; height: 194px;
    border-radius: 50%; border: 11px solid #4f8a8c;
    background: radial-gradient(circle at 50% 45%, #b98d6c 0%, #6b5444 55%, #2c2520 100%);
  }
  .awards-title {
    position: absolute; left: 363px; top: 324px; width: 317px; text-align: center;
    font-size: 15px; font-weight: 800; color: var(--gold-text);
  }
  .awards-list {
    position: absolute; left: 363px; top: 355px; width: 317px; text-align: center;
    font-size: 8.8px; font-weight: 700; line-height: 12px;
  }
  .badge { position: absolute; top: 390px; }
  .badge--round { width: 46px; height: 46px; border-radius: 50%; }
  .badge--quality { left: 435px; background: var(--badge-blue); }
  .badge--profile { left: 520px; background: var(--badge-sky); }
  .badge--coach { left: 576px; top: 391px; width: 94px; height: 40px; border-radius: 3px; background: var(--badge-grey); }

  /* ---------- Inside ---------- */
  .emblem {
    position: absolute; left: 4px; top: 8px; width: 74px; height: 70px;
    border-radius: 50%; background: var(--sand);
  }
  .fields-title {
    position: absolute; left: 96px; top: 6px; width: 160px; text-align: center;
    font-size: 15px; font-weight: 700; color: var(--teal-dark);
  }
  .fields-lead {
    position: absolute; left: 86px; top: 40px; width: 180px; text-align: center;
    font-size: 12px; font-weight: 700; line-height: 16px; letter-spacing: 0.6px;
    color: var(--gold);
  }
  .fields-list {
    position: absolute; left: 318px; top: 7px; width: 350px; list-style: none;
    font-size: 6.6px; font-weight: 700; line-height: 8.9px;
  }
  .fields-list li { padding-left: 8px; text-indent: -8px; }
  .fields-list li::before { content: "– "; }
  .diagram-area {
    position: absolute; left: 15px; top: 131px; width: 220px; height: 200px;
    border-radius: 50%; background: var(--sand);
  }
  .connectors { position: absolute; left: 0; top: 80px; width: 300px; height: 360px; }
  .service-label {
    position: absolute; font-size: 11.5px; font-weight: 700; color: var(--teal-dark);
  }
  .service-box {
    position: absolute; background: var(--sand-light); border-radius: 7px;
    font-size: 5.7px; font-weight: 700; line-height: 7.9px; text-align: justify;
  }
</style>
</head>
<body>

<section class="page page--outside">
  <div class="qual-panel">
    <h1 class="qual-title"><span class="dot"></span>Qualifikation<span class="dot"></span></h1>
    <div class="qual-list">
      <div class="entry"><div class="entry-title">Dipl. Betriebswirt</div><div class="entry-place">Mainufer Hochschule für Finanzen und Management – 4 Jahre</div></div>
      <div class="entry"><div class="entry-title accent">Bankkaufmann IHK</div></div>
      <div class="entry"><div class="entry-place">Coach (BVC)</div><div class="entry-place">kobra – Kreis für Beratungs- und Organisationskompetenz - 2 Jahre</div></div>
      <div class="entry"><div class="entry-title accent">Wirtschaftsmediator</div><div class="entry-place">NORDWIND Hochschule Seestadt - 2 Jahre</div></div>
      <div class="entry"><div class="entry-title">General Management</div><div class="entry-place">Programm VK BANK Gruppe - 2 Jahre ESGF Berlin</div></div>
    </div>
  </div>

  <h2 class="contact-title">Kontakt</h2>
  <div class="contact-frame"></div>
  <address class="contact-card">
    <span>Jonas Lindner</span>
    <span>Lindenallee 5</span>
    <span>63599 Waldhain</span>
  </address>

  <svg class="footer-bands" viewBox="0 0 380 60" aria-hidden="true">
    <polygon points="0,0 380,0 372,8 0,8" fill="#b89a55"/>
    <polygon points="0,21 380,21 352,58 0,58" fill="#b89a55"/>
  </svg>
  <div class="footer-info">
    <div>Phone: +49 170 4412873</div>
    <div>Mail: jlindner@quervoran.kollegen</div>
    <div>Web: www://quervoran.kollegen</div>
  </div>

  <div class="brand"><span class="mark"></span>quervoran.kollegen</div>
  <div class="tagline">BERATUNG I COACHING I MEDIATION</div>

  <div class="portrait" role="img" aria-label="Porträtfoto des Beraters"></div>

  <h2 class="awards-title">Zertifizierungen &amp; Auszeichnungen</h2>
  <div class="awards-list">
    <div>Preisträger Fachpreis Lernkultur 2004</div>
    <div>–Preisträger Fachpreis Personalarbeit 2007</div>
  </div>
  <div class="badge badge--round badge--quality" role="img" aria-label="Qualitätssiegel Weiterbildung"></div>
  <div class="badge badge--round badge--profile" role="img" aria-label="Zertifikat Persönlichkeitsprofil"></div>
  <div class="badge badge--coach" role="img" aria-label="Zertifizierter Coach"></div>
</section>

<section class="page page--inside">
  <div class="emblem" role="img" aria-label="Dekoratives Kreiselement"></div>
  <h2 class="fields-title">Erfahrungsfelder</h2>
  <p class="fields-lead">Seit über 20 Jahren in großen Inhouseprojekten und als externer Berater und Coach tätig.</p>
  <ul class="fields-list">
    <li>Aufsichtsratsmandate in der Beratungsbranche für interaktive Lernmedien seit 2001 und im betrieblichen Gesundheitsmanagement seit 2012</li>
    <li>Sparingspartner und Berater für Vorstand und Aufsichtsrat</li>
    <li>Verantwortung für unternehmensweite Restrukturierungen und Personalabbau</li>
    <li>Leitung von Kostensenkungs- und Effizienssteigerungsprojekten</li>
    <li>Krisenmanagement, Krisenkommunikation</li>
    <li>Leitung von mehrjährigen Changemanagementprojekten</li>
    <li>Aufbau und Neuausrichtung von Organisationseinheiten</li>
    <li>Führung von Einheiten mit über 200 Mitarbeitern</li>
  </ul>

  <svg class="connectors" viewBox="0 0 300 360" aria-hidden="true">
    <g stroke="#236a70" stroke-width="1.4">
      <line x1="200" y1="95" x2="265" y2="10"/>
      <line x1="235" y1="149" x2="284" y2="149"/>
      <line x1="205" y1="205" x2="265" y2="234"/>
      <line x1="160" y1="240" x2="208" y2="321"/>
    </g>
  </svg>
  <div class="diagram-area" role="img" aria-label="Grafik: Leistungsbereiche im Überblick"></div>

  <h3 class="service-label" style="left:293px; top:87px;">Meine Leistungen</h3>
  <p class="service-box" style="left:283px; top:103px; width:368px; height:69px; padding:3px 8px 3px 27px;">Ich unterstütze Führungspersonen in Spitzenpositionen bei: Erfolgreicher Bewältigung anspruchsvoller Managementphasen. Übernahme einer neuen Position, herausfordernden strategischen Implementierungen, Turnaroundsituationen. Begleitung in Konflikten im obersten Führungsteam, sensiblen personellen Einzelsituationen auf den Topebenen und bei der Umsetzung personalpolitisch herausfordernder Maßnahmen. Moderation von Konflikten zwischen Eigentümer, Aufsichtsgremium und oberster Führungsebene. Zielgruppen: Top-Führungspersonen, Vorstände und Aufsichtsräte. Tätigkeitsbereiche: Coaching, Executive Advisory, Restrukturierungen und Change Management.</p>

  <h3 class="service-label" style="left:321px; top:178px;">Position Counseling</h3>
  <p class="service-box" style="left:310px; top:196px; width:360px; height:62px; padding:12px 10px 4px 27px;">Individuelle Einzelberatung, die sich ganz mit der Person und dem Kontext der aktuellen Herausforderungen befasst. 360°-Check auf alle vernetzten (Teil-)Aspekte von Managementthemen, Transformations-Prozesse und mikropolitischen Verhältnissen. Trittsicherheit und die Festigung der aktuellen Position stehen hierbei im Mittelpunkt meiner Unterstützungsleistungen.</p>

  <h3 class="service-label" style="left:295px; top:270px;">Coaching</h3>
  <p class="service-box" style="left:283px; top:288px; width:369px; height:62px; padding:12px 22px 4px 39px;">Professionelle Beratung, Begleitung und Unterstützung zur Steigerung und dem Erhalt der Leistungsfähigkeit. Im Coaching unterstütze ich die persönliche und berufliche Weiterentwicklung, die Selbstorganisation und das Selbstverständnis. Der Klient erhält die Möglichkeit, über sich selbst nachzudenken, neue Fähigkeiten zu erlernen und neue Perspektiven einzunehmen.</p>

  <h3 class="service-label" style="left:248px; top:353px;">Mediation</h3>
  <p class="service-box" style="left:231px; top:372px; width:369px; height:58px; padding:3px 28px 3px 46px; text-align:left;">Unterstützung bei Konfliktlösungen, die für alle Beteiligten gewinnbringend und daher nachhaltig sind. Professionelle Begleitung unter anderem bei allen kritischen Themen der Mitarbeiterführung bis hin zu Ausscheidensvereinbarungen und Kündigungen, bei Differenzen im Zusammenhang mit Umstrukturierungen, Fusionen, Unternehmensnachfolgen, bei Verhandlungen mit den Personalvertretungen und Unstimmigkeiten innerhalb einer oder zwischen mehreren Organisationseinheiten und vielem mehr.</p>
</section>

</body>
</html>
```